EXTENDED Store hours to serve your healthcare needs

I'M LOOKING FOR A NICE FLYER THAT SHOWS THE FOLLOWING INFORMATION:

Logo
address
tel phone and fax
email address

Extending our hours to meet the growing healthcare needs of our community. Fast delivery service!

Monday - Thursday 10am-midnight
Friday 10am-4pm
Saturday - Motzei Shabbos till midnight
Sunday 10am-7pm

Target Market(s)

Community

Industry/Entity Type

Pharmacy

Requirements
Must have
• Extended hours
• personal care
• expert advice
• superior service
Nice to have
• Looking for no people pictures
• Eye popping design
• Classic modern clean design
Should not have
• store description is services
• And should not say Fiirst to open and last to close

```html
<!DOCTYPE html>
<html lang="en">
<head>
<meta charset="utf-8">
<title>K. Lane Pharmacy – Extended Hours</title>
<link rel="stylesheet" href="https://fonts.googleapis.com/css2?family=Montserrat:wght@700;800;900&family=Raleway:wght@400;500;600;700&display=swap">
<style>
  :root {
    --blue: #1565b4;
    --blue-deep: #0d4f98;
    --blue-band: #0e4a8e;
    --red: #b0232b;
    --ink: #2b2b2b;
    --white: #ffffff;
    --shelf-light: #f1f3f5;
    --shelf-mid: #dfe4e8;
  }
  * { margin: 0; padding: 0; box-sizing: border-box; }
  html, body { width: 846px; height: 1200px; overflow: hidden; background: #fff; }
  .flyer {
    position: relative; width: 846px; height: 1200px; overflow: hidden;
    font-family: "Raleway", sans-serif; color: var(--white);
  }
  .store-photo {
    position: absolute; left: 0; top: 0; width: 846px; height: 860px;
    background: radial-gradient(ellipse at 72% 48%, #e9e3dc 0%, rgba(233,227,220,0) 38%),
                linear-gradient(100deg, var(--shelf-mid) 0%, var(--shelf-light) 45%, #f7f8f9 100%);
  }
  .shapes { position: absolute; left: 0; top: 0; }
  .brand {
    position: absolute; left: 0; width: 846px; top: 100px; text-align: center;
    font-family: "Raleway", sans-serif; font-weight: 700; font-size: 44px;
    color: var(--blue); letter-spacing: 1px;
  }
  .brand .mark {
    display: inline-block; width: 30px; height: 30px; background: var(--blue);
    margin-right: 14px; vertical-align: -2px;
  }
  .promise {
    position: absolute; left: 0; width: 846px; top: 170px; text-align: center;
    font-size: 18px; font-weight: 600; letter-spacing: 2px; color: var(--ink);
  }
  .promise .dot { color: var(--red); margin: 0 10px; }
  .feature { position: absolute; left: 72px; color: var(--ink); }
  .feature .lead { font-family: "Raleway", sans-serif; font-weight: 500; font-size: 31px; letter-spacing: 1px; line-height: 1; }
  .feature .big { font-family: "Montserrat", sans-serif; font-weight: 900; font-size: 56px; line-height: 1; letter-spacing: -1px; margin-top: 4px; }
  .feature-delivery { top: 272px; }
  .feature-delivery .big { color: var(--blue); }
  .feature-advice { top: 395px; }
  .feature-advice .big { color: var(--red); }
  .extending { position: absolute; left: 37px; top: 640px; }
  .extending h1 { font-family: "Montserrat", sans-serif; font-weight: 800; font-size: 46px; letter-spacing: -1px; line-height: 1.1; }
  .extending p { font-size: 26px; line-height: 40px; margin-top: 4px; font-weight: 500; }
  .hours { position: absolute; left: 37px; top: 878px; width: 390px; }
  .hours .day { height: 80px; position: relative; }
  .hours .label { position: absolute; left: 26px; top: 0; font-size: 19px; font-weight: 500; letter-spacing: .5px; }
  .hours .rule { position: absolute; left: 0; right: 0; top: 31px; border-top: 1.5px solid var(--white); }
  .hours .rule::before { content: ""; position: absolute; left: 10px; top: -4px; width: 8px; height: 6px; background: var(--white); }
  .hours .time {
    position: absolute; left: 0; right: 0; top: 33px; height: 36px; padding: 6px 5px 0 0;
    text-align: right; font-family: "Montserrat", sans-serif; font-weight: 700; font-size: 22px;
  }
  .hours .alt .time { background: var(--blue-band); }
  .social { position: absolute; left: 670px; top: 851px; display: flex; align-items: center; gap: 6px; font-size: 17px; }
  .social .label { margin-right: 12px; }
  .social .box { width: 27px; height: 27px; background: var(--white); }
  .contact { position: absolute; left: 492px; top: 948px; list-style: none; font-size: 22px; font-weight: 500; }
  .contact li { display: flex; align-items: flex-start; line-height: 32px; }
  .contact li svg { flex: none; margin: 8px 14px 0 0; }
  .contact .gap { margin-bottom: 24px; }
  .contact b { font-weight: 700; }
</style>
</head>
<body>
<div class="flyer">
  <div class="store-photo" role="img" aria-label="Bright pharmacy interior with shelves of products, softly out of focus"></div>

  <svg class="shapes" width="846" height="1200" viewBox="0 0 846 1200" aria-hidden="true">
    <polygon points="0,512 310,610 0,565" fill="var(--red)"/>
    <polygon points="376,750 846,700 846,850 700,760 396,805" fill="var(--red)"/>
    <polygon points="0,565 310,610 396,805 700,760 846,850 846,1200 0,1200" fill="var(--blue)"/>
    <polygon points="396,805 700,760 846,850 846,1200 560,1200" fill="var(--blue-deep)" opacity=".35"/>
    <polygon points="37,278 50,287 37,296" fill="var(--red)"/>
    <polyline points="170,286 420,286 420,334" fill="none" stroke="var(--red)" stroke-width="2"/>
    <polygon points="420,326 410,334 420,342" fill="var(--red)"/>
    <polygon points="37,400 50,409 37,418" fill="var(--blue)"/>
    <polyline points="220,408 420,408 420,455" fill="none" stroke="var(--blue)" stroke-width="2"/>
    <polygon points="420,447 410,455 420,463" fill="var(--blue)"/>
  </svg>

  <div class="brand"><span class="mark"></span>K. Lane Pharmacy</div>
  <div class="promise">PERSONAL CARE<span class="dot">•</span>SUPERIOR SERVICE</div>

  <div class="feature feature-delivery"><div class="lead">FAST</div><div class="big">DELIVERY</div></div>
  <div class="feature feature-advice"><div class="lead">EXPERT</div><div class="big">ADVICE</div></div>

  <div class="extending">
    <h1>Extending</h1>
    <p>our hours to meet the<br>growing healthcare<br>needs of our community.</p>
  </div>

  <div class="hours">
    <div class="day"><span class="label">MONDAY – THURSDAY</span><span class="rule"></span><div class="time">10am-Midnight</div></div>
    <div class="day alt"><span class="label">FRIDAY</span><span class="rule"></span><div class="time">10am-4pm</div></div>
    <div class="day"><span class="label">SATURDAY</span><span class="rule"></span><div class="time">Motzei Shabbos till midnight</div></div>
    <div class="day alt"><span class="label">SUNDAY</span><span class="rule"></span><div class="time">10am-7pm</div></div>
  </div>

  <div class="social"><span class="label">Join us:</span><span class="box"></span><span class="box"></span></div>

  <ul class="contact">
    <li class="gap">
      <svg width="16" height="18" viewBox="0 0 16 18"><rect width="16" height="18" rx="3" fill="#fff"/><circle cx="8" cy="7" r="3" fill="var(--blue)"/><path d="M8 15 L4 8 H12 Z" fill="var(--blue)"/></svg>
      <span>482 Alder Ave<br>Riverton, NY 10955</span>
    </li>
    <li>
      <svg width="16" height="16" viewBox="0 0 16 16"><rect width="16" height="16" rx="3" fill="#fff"/><path d="M4 3 L6.5 3 L7.5 6 L6 7 Q7 9.5 9 10 L10 8.5 L13 9.5 L13 12 Q8 13 4 8 Z" fill="var(--blue)"/></svg>
      <span>(555) 310-2246</span>
    </li>
    <li>
      <svg width="16" height="16" viewBox="0 0 16 16"><rect width="16" height="16" rx="3" fill="#fff"/><rect x="4" y="3" width="8" height="4" fill="var(--blue)"/><rect x="3" y="8" width="10" height="5" fill="var(--blue)"/></svg>
      <span>(555) 310-2247</span>
    </li>
    <li>
      <svg width="16" height="16" viewBox="0 0 16 16"><rect width="16" height="16" rx="3" fill="#fff"/><rect x="3" y="4.5" width="10" height="7" fill="none" stroke="var(--blue)" stroke-width="1.4"/><polyline points="3,4.5 8,9 13,4.5" fill="none" stroke="var(--blue)" stroke-width="1.4"/></svg>
      <span>klanepharmacy@mail.com</span>
    </li>
    <li>
      <svg width="16" height="16" viewBox="0 0 16 16"><rect width="16" height="16" rx="3" fill="#fff"/><circle cx="8" cy="8" r="5" fill="none" stroke="var(--blue)" stroke-width="1.2"/><ellipse cx="8" cy="8" rx="2.2" ry="5" fill="none" stroke="var(--blue)" stroke-width="1.2"/><line x1="3" y1="8" x2="13" y2="8" stroke="var(--blue)" stroke-width="1.2"/></svg>
      <span>www.<b>klanepharmacy</b>.com</span>
    </li>
  </ul>
</div>
</body>
</html>
```